ALL TEXT Social Media Graphics

We are looking for a series of social media graphics for Instagram (new size: 4:5 (1080 x 1350 pixels) ratio that are ALL TEXT. We want the following quotes below on each graphic; one quote per graphic. AND, In very small letters at the bottom of each graphic, add @PaulaWrenLive
The look and feel of these graphics should be complimentary to the color palette attached below; but keep them simple. But the design is up to you; at the end of this document, I provided various samples of all text graphics that I like as examples.
The Quotes are in the attached WORD document
women trying to lose weight

```html
<!DOCTYPE html>
<html lang="en">
<head>
<meta charset="utf-8">
<title>Summer Reset Social Series</title>
<link href="https://fonts.googleapis.com/css2?family=Bebas+Neue&family=Lato:ital,wght@0,400;0,700;0,900;1,400&display=swap" rel="stylesheet">
<style>
  :root {
    --backdrop: #1f1f1f;
    --card: #ffffff;
    --pink: #f06595;
    --magenta: #b0185a;
  }
  * { box-sizing: border-box; margin: 0; padding: 0; }
  html, body { width: 1200px; height: 904px; overflow: hidden; background: var(--backdrop); }
  .board { position: relative; width: 1200px; height: 904px; }
  .post {
    position: absolute; background: var(--card);
    display: flex; flex-direction: column; align-items: center;
    text-align: center; font-family: "Lato", sans-serif; color: var(--magenta);
  }
  .post--feature { left: 35px; top: 45px; width: 463px; height: 579px; padding: 28px 30px 0; }
  .post--tile { width: 208px; height: 260px; padding: 11px 10px 0; }
  .col-1 { left: 516px; } .col-2 { left: 739px; } .col-3 { left: 965px; }
  .row-1 { top: 45px; } .row-2 { top: 322px; } .row-3 { top: 596px; }

  .lead { font-size: 11px; line-height: 1.25; }
  .lead--strong { font-size: 14px; font-weight: 700; line-height: 1.3; }
  .headline {
    font-family: "Bebas Neue", sans-serif; font-size: 28px; line-height: 0.93;
    margin-top: 10px; letter-spacing: 0.2px;
  }
  .pink { color: var(--pink); }
  .magenta { color: var(--magenta); }
  .cta { font-size: 13px; font-weight: 700; line-height: 1.2; margin-top: 12px; text-transform: uppercase; }
  .cta--ruled { border-top: 1px solid var(--magenta); border-bottom: 1px solid var(--magenta); padding: 4px 2px; }
  .cta--small { font-size: 12px; }
  .cta--badge { background: var(--pink); color: #fff; padding: 2px 6px; margin-top: 6px; font-weight: 700; }
  .handle { font-size: 8px; font-style: italic; margin-top: auto; margin-bottom: 16px; }

  .post--feature .lead { font-size: 23px; line-height: 1.28; }
  .post--feature .headline { font-size: 64px; line-height: 0.92; margin-top: 34px; color: var(--pink); }
  .post--feature .cta-intro { font-size: 28px; margin-top: 40px; }
  .post--feature .cta-name { font-size: 29px; font-weight: 900; line-height: 1.2; }
  .post--feature .handle { font-size: 19px; margin-bottom: 38px; }
</style>
</head>
<body>
<main class="board">
  <article class="post post--feature">
    <p class="lead">You can absolutely be down 20–30 pounds by end of summer.</p>
    <h1 class="headline">All it takes is<br>the right plan-<br>and you’ve<br>found it.</h1>
    <p class="cta-intro">Comment “Sun Glow” for the</p>
    <p class="cta-name">SUN GLOW SUMMER<br>RESET!</p>
    <p class="handle">@PaulaWrenLive</p>
  </article>

  <article class="post post--tile col-1 row-1">
    <p class="lead">You don’t need another diet -<br>you need a system that works.</p>
    <h2 class="headline pink">Drop 30<br>pounds with<br>the Sunglow<br>summer<br>reset</h2>
    <p class="cta">Comment “Summer”<br>to start now.</p>
    <p class="handle">@PaulaWrenLive</p>
  </article>

  <article class="post post--tile col-2 row-1">
    <p class="lead">This summer ain’t over—<br>and neither are your body goals.</p>
    <h2 class="headline pink">Drop 30<br>pounds with<br>the Sun Glow<br>summer<br>reset</h2>
    <p class="cta">Comment “Sun Glow”<br>to get the plan</p>
    <p class="handle">@PaulaWrenLive</p>
  </article>

  <article class="post post--tile col-3 row-1">
    <h2 class="headline magenta" style="margin-top:2px;font-size:26px">If your goal<br>is a tiny waist,<br>flat belly,<br>and 30 pounds<br>down-this is<br>the plan</h2>
    <p class="cta cta--ruled cta--small" style="margin-top:8px">Comment “Summer”<br>to join the Sun Glow<br>Summer Reset!</p>
    <p class="handle">@PaulaWrenLive</p>
  </article>

  <article class="post post--tile col-1 row-2">
    <p class="lead lead--strong">There’s still time to drop<br>the 30 pounds and slay<br>this summer.</p>
    <h2 class="headline magenta">The Sun<br>Glow Summer<br>Reset has<br>the blueprint.</h2>
    <p class="cta cta--badge">Comment “Sun Glow”!</p>
    <p class="handle">@PaulaWrenLive</p>
  </article>

  <article class="post post--tile col-2 row-2">
    <p class="lead lead--strong" style="font-size:13px">Snatched waist, flat tummy,<br>30 pounds lighter —</p>
    <h2 class="headline pink" style="font-size:25px">That’s what<br>the Sun Glow<br>Summer Reset<br>challenge<br>delivers</h2>
    <p class="cta cta--ruled" style="margin-top:10px">Comment “Sun Glow”<br>to get the plan</p>
    <p class="handle">@PaulaWrenLive</p>
  </article>

  <article class="post post--tile col-3 row-2">
    <p class="lead">Nothing feels better than seeing<br>that scale drop week after week.</p>
    <h2 class="headline pink">Let’s lose<br>up to 30 pounds<br>this summer-<br>together.</h2>
    <p class="cta cta--ruled cta--small">Comment “Summer”<br>to join the Sun Glow<br>Summer Reset!</p>
    <p class="handle">@PaulaWrenLive</p>
  </article>

  <article class="post post--tile col-1 row-3">
    <p class="lead lead--strong" style="font-size:13px;font-weight:400">Sis, we’re dropping belly<br>flat and saying goodbye<br>to stubborn pounds</p>
    <h2 class="headline pink" style="font-size:34px;margin-top:8px">Join the<br>Sun Glow<br>Summer<br>Reset</h2>
    <p class="cta cta--ruled" style="margin-top:6px">Comment “Summer”</p>
    <p class="handle">@PaulaWrenLive</p>
  </article>

  <article class="post post--tile col-2 row-3">
    <p class="lead lead--strong pink" style="font-size:13px;font-weight:400">Don’t wait ‘til next<br>summer to get right.<br>The time is NOW.</p>
    <h2 class="headline magenta" style="margin-top:6px">Drop 30<br>pounds with<br>the Sun Glow<br>summer<br>reset</h2>
    <p class="cta cta--ruled pink" style="margin-top:6px">Comment “Summer”</p>
    <p class="handle">@PaulaWrenLive</p>
  </article>

  <article class="post post--tile col-3 row-3">
    <p class="lead pink">You’ve got 8 weeks and the perfect<br>plan to drop 30 pounds.</p>
    <h2 class="headline magenta">Let’s get<br>snatched this<br>summer with<br>the Sun Glow<br>summer<br>reset</h2>
    <p class="cta cta--ruled" style="margin-top:8px">Comment “Summer”</p>
    <p class="handle">@PaulaWrenLive</p>
  </article>
</main>
</body>
</html>
```